Coffee roastery and coffee shop needs a packaging design

We need a packaging design for an our company we sell coffee beans for coffee shops . and we have a coffee shop . our company name is (BRAMBLE ROASTERY) we are based in UAE. We want a cup design for cold coffee and hot and coffee bag design and paper bag design. I uploaded our logo design.

```html
<!DOCTYPE html>
<html lang="en">
<head>
<meta charset="utf-8">
<title>Bramble Roastery – Cold Coffee Bag</title>
<link href="https://fonts.googleapis.com/css2?family=Montserrat:wght@300;400;600;700;800&family=Kaushan+Script&display=swap" rel="stylesheet">
<style>
  :root {
    --backdrop: #d6d6d6;
    --bag-black: #161616;
    --brand-green: #3aa94a;
    --ink-white: #f4f4f4;
    --ink-grey: #bdbdbd;
  }
  html, body {
    margin: 0;
    width: 1200px;
    height: 901px;
    overflow: hidden;
    background: var(--backdrop);
  }
  .canvas {
    position: relative;
    width: 1200px;
    height: 901px;
    background: radial-gradient(ellipse at 50% 40%, #e4e4e4 0%, var(--backdrop) 75%);
  }
  .bag-front {
    position: absolute;
    left: 410px;
    top: 130px;
    width: 380px;
    height: 640px;
    background: var(--bag-black);
    overflow: hidden;
    font-family: "Montserrat", sans-serif;
    color: var(--ink-white);
    text-align: center;
  }
  .green-band {
    position: absolute;
    left: 160px;
    top: 0;
    width: 82px;
    height: 210px;
    background: var(--brand-green);
  }
  .brand-name {
    position: absolute;
    top: 250px;
    left: 0;
    right: 0;
  }
  .brand-name .word {
    display: block;
    font-weight: 400;
    font-size: 26px;
    letter-spacing: 7px;
    padding-left: 7px;
  }
  .brand-name .sub {
    display: block;
    margin-top: 2px;
    font-weight: 300;
    font-size: 9px;
    letter-spacing: 6px;
    padding-left: 6px;
    color: var(--ink-grey);
  }
  .product-title {
    position: absolute;
    top: 360px;
    left: 0;
    right: 0;
  }
  .product-title .script {
    display: block;
    font-family: "Kaushan Script", cursive;
    color: var(--brand-green);
    font-size: 72px;
    line-height: 1;
  }
  .product-title .caps {
    display: block;
    font-weight: 700;
    font-size: 44px;
    letter-spacing: 1px;
    line-height: 1.1;
  }
  .facts {
    position: absolute;
    top: 520px;
    left: 50px;
    right: 50px;
    display: flex;
    justify-content: center;
    padding-bottom: 10px;
    border-bottom: 1px solid var(--brand-green);
  }
  .facts .fact {
    padding: 0 18px;
    line-height: 1.15;
  }
  .facts .fact + .fact {
    border-left: 1px solid var(--ink-grey);
  }
  .facts .big {
    display: block;
    font-weight: 800;
    font-size: 15px;
    color: var(--brand-green);
  }
  .facts .small {
    display: block;
    font-weight: 400;
    font-size: 11px;
  }
  .weight-pill {
    position: absolute;
    left: 155px;
    bottom: 0;
    width: 70px;
    height: 42px;
    border-radius: 18px 18px 0 0;
    background: var(--brand-green);
    color: var(--bag-black);
    font-weight: 600;
    font-size: 14px;
    line-height: 40px;
  }
</style>
</head>
<body>
<main class="canvas">
  <section class="bag-front">
    <div class="green-band"></div>
    <div class="brand-name">
      <span class="word">BRAMBLE</span>
      <span class="sub">ROASTERY</span>
    </div>
    <h1 class="product-title" style="margin:0">
      <span class="script">Cold</span>
      <span class="caps">COFFEE</span>
    </h1>
    <div class="facts">
      <div class="fact"><span class="big">100%</span><span class="small">ARABICA</span></div>
      <div class="fact"><span class="big">UAE</span><span class="small">COFFEE BEANS</span></div>
    </div>
    <div class="weight-pill">500 g</div>
  </section>
</main>
</body>
</html>
```